Plakate für eine Selbstverteidigungs- und Selbstbehauptungsschule
Zielgruppe
Wir sind eine Selbstverteidigungs- und Selbstbehauptungsschule (Krav-Maga) in Hessen (Darmstadt und Rödermark). Wir haben uns darauf spezialisiert, den Menschen zu helfen ihre verschütteten Verteidigungsinstinkte wieder zu entdecken. So wie eine Katze sich von Natur aus verteidigen kann so ist es auch bei uns Menschen. Nur wurde dies uns im Laufe unserer Erziehung und Schulbildung aberzogen. Wir geben den Menschen ihre natürliche Selbstsicherheit zurück. Das sollte so auch deutlich aus der Werbung hervorgehen und auf die Lesenden überspringen.
Zielgruppe sind Menschen, die mit ihrem Selbstbewusstsein hadern (Schüchternheit, Unsicherheit) oder die ihr Selbstvertrauen noch weiter ausbauen wollen. In dieser Werbekampagne geht erstmal nur um Erwachsene.
Der von uns angebotene Kurs heißt: Felsa-Runo-Klar (Pure bedeutet, dass wir Selbstverteidigungstechniken vermitteln, die in leicht zu erlernen und demzufolge in etwaigen Notsituationen auch intuitiv/leicht anzuwenden sind).
Aufgabenstellung
Ich brauche eine neue, ansprechende Werbekampagne für Plakate/Social Media/Flyer, die auf die Wichtigkeit des Themas eingeht und seriös rüberkommt. Wir sind nicht die 'Türsteher' oder 'Schwarz-Gekleideten', sondern eine seriöse Kampfsportschule, die aus eigenen Erfahrungen heraus und mit Leidenschaft unterrichtet. Daher soll die Werbung hochwertig, zielgruppenorientiert und themenfokussiert sein - ähnlich wie bei Autowerbung oder Kosmetik. Sie können sich das so vorstellen, dass wir Selbstvertrauen verkaufen - daher sollte der Fokus darauf liegen, und nicht auf dem Kurs/Sportangebot als solches.
Eine Idee, um das Thema Selbstvertrauen stärker hervorzuheben und auf die Deutlichkeit der angeborenen Verteidigungsinstinkte einzugehen, ist das Aufgreifen unserer Tier-Symbolik auf der Webseite unter https://www.felsa-runo-halt.de/felsa-runo-klar Gerne aber auch eigene Ideen einbringen.
Text Ideen von mir vorab, um Ihnen meine gewünschte Richtung zu verdeutlichen:
- Wecke die Löwin in dir!
- Wecke den Tiger in dir!
- Wecke deine Stärke!
- Stärke dein Selbst!
- Wecke deine Kräfte!
- Werde dein eigener Bodyguard! u.s.w.
Türkis
C:80 M:2 Y:24 K:0
R:0 G:172 B:195
Hex color #00ACC3
gray solid color background:
C:0 M:0 Y:0 K:72,35
R:71 G:71 B:71
Hex color #474747
gray color for white background version:
C:0 M:0 Y:0 K:58
R:140 G:140 B:139
Hex color #8c8c8b
black:
C:91,25 M:78,76 Y:61,98 K:97,47
R:0 G:0 B:0
Hex color #000000
white:
C:0 M:0 Y:0 K:0
R:255 G:255 B:255
Hex color #ffffff
Kind regards
Weitere Logos und Schrifttypen kann ich noch zur Verfügung stellen.
Die Entwürfe müssen in einem Format sein, sodass wir sie später selbst bearbeiten oder anpassen können.

```html
<!DOCTYPE html>
<html lang="de">
<head>
<meta charset="utf-8">
<title>Felsa-Runo-Klar Plakate</title>
<link rel="stylesheet" href="https://fonts.googleapis.com/css2?family=Oswald:wght@300;400;500&family=Barlow+Condensed:wght@400;800&family=Montserrat:wght@700&display=swap">
<style>
:root{
  --teal:#00acc3;
  --gray:#474747;
  --white:#ffffff;
  --black:#000000;
  --page:#ffffff;
}
*{margin:0;padding:0;box-sizing:border-box}
html,body{width:1200px;height:818px;overflow:hidden;background:var(--page)}
.canvas{position:relative;width:1200px;height:818px}
.poster{position:absolute;top:34px;width:530px;height:751px;background:var(--gray);overflow:hidden;color:var(--white)}
.poster--lioness{left:37px}
.poster--tiger{left:632px}
.poster__photo{position:absolute;left:0;top:95px;width:530px;height:560px}
.poster--lioness .poster__photo{
  background:
    linear-gradient(to bottom,var(--gray) 0%,rgba(71,71,71,0) 20%,rgba(71,71,71,0) 78%,var(--gray) 100%),
    linear-gradient(to right,#3a2a22 0%,#8a5b45 22%,#5a4a3c 42%,#b89068 62%,#c9a277 80%,#7a5a3c 100%);
}
.poster--tiger .poster__photo{
  background:
    linear-gradient(to bottom,var(--gray) 0%,rgba(71,71,71,0) 20%,rgba(71,71,71,0) 78%,var(--gray) 100%),
    linear-gradient(to right,#2a2420 0%,#8a5a40 20%,#4a4038 40%,#3a5a78 52%,#b87a3a 68%,#d89a50 85%,#6a4a2a 100%);
}
.badge{position:absolute;left:29px;top:26px;width:108px;height:108px;border-radius:50%;background:var(--teal);
  display:flex;align-items:center;justify-content:center;text-align:center}
.badge__text{font-family:"Oswald",sans-serif;font-weight:400;font-size:15.5px;line-height:1.22;transform:rotate(-10deg)}
.headline{position:absolute;left:155px;top:22px;font-family:"Oswald",sans-serif;font-weight:300;text-transform:uppercase;line-height:1;
  text-shadow:0 2px 6px rgba(0,0,0,.45)}
.headline__intro{display:block;font-size:56px;letter-spacing:.5px}
.headline__animal{display:block;font-size:96px;color:var(--teal);margin-top:4px;line-height:.98}
.headline__close{display:block;font-size:98px;line-height:.98}
.brand{position:absolute;left:0;width:100%;text-align:center}
.brand__name{top:596px;font-family:"Barlow Condensed",sans-serif;font-weight:800;font-size:48px;line-height:1;letter-spacing:.2px}
.brand__claim{top:644px;font-family:"Montserrat",sans-serif;font-weight:700;font-size:25px;letter-spacing:1.3px;line-height:1}
.contact{position:absolute;left:0;width:100%;top:680px;text-align:center;font-family:"Barlow Condensed",sans-serif;font-weight:400;font-size:11.5px;line-height:15px;color:#e8e8e8}
.web{position:absolute;left:0;width:100%;top:717px;text-align:center;font-family:"Oswald",sans-serif;font-weight:500;font-size:16px;line-height:1}
</style>
</head>
<body>
<div class="canvas">

  <section class="poster poster--lioness">
    <div class="poster__photo" role="img" aria-label="Porträt einer entschlossenen Frau neben dem Kopf einer Löwin mit türkisfarbenen Augen"></div>
    <div class="badge"><p class="badge__text">Jetzt<br>Probetraining<br>buchen!</p></div>
    <h1 class="headline">
      <span class="headline__intro">Wecke die</span>
      <span class="headline__animal">Löwin</span>
      <span class="headline__close">in dir!</span>
    </h1>
    <p class="brand brand__name">FELSA-RUNO-KLAR</p>
    <p class="brand brand__claim">SELBSTSICHER WERDEN</p>
    <p class="contact">Kampfkunst- &amp; Fitnesskurse – Tove Sreki | Lindenweg 12 | 63999 Talbrunn<br>Telefon: 0151/ 47310926 | info@felsa-runo-halt.de</p>
    <p class="web">www.FELSA-RUNO-KLAR.de</p>
  </section>

  <section class="poster poster--tiger">
    <div class="poster__photo" role="img" aria-label="Porträt eines entschlossenen Mannes neben dem Kopf eines Tigers mit türkisfarbenen Augen"></div>
    <div class="badge"><p class="badge__text">Jetzt<br>Probetraining<br>buchen!</p></div>
    <h1 class="headline">
      <span class="headline__intro">Wecke den</span>
      <span class="headline__animal">Tiger</span>
      <span class="headline__close">in dir!</span>
    </h1>
    <p class="brand brand__name">FELSA-RUNO-KLAR</p>
    <p class="brand brand__claim">SELBSTSICHER WERDEN</p>
    <p class="contact">Kampfkunst- &amp; Fitnesskurse – Tove Sreki | Lindenweg 12 | 63999 Talbrunn<br>Telefon: 0151/ 47310926 | info@felsa-runo-halt.de</p>
    <p class="web">www.FELSA-RUNO-KLAR.de</p>
  </section>

</div>
</body>
</html>
```